Lumen Keyvault Password Manager WebApp Design

Lumen Keyvault is seeking an expert UI designer to provide a fresh and modern visual appeal for our product. Our inspiration comes from two major tools that have successfully managed to balance functionality and design aesthetics - Orbix Folder and Vaultmint. We want our application to exude a similar trustworthiness and modernity, through a clean, intuitive and responsive design.
We have established preliminary mockups and would like the designer to work within these parameters while enhancing the overall user experience. The primary tasks will involve innovative and improved designs of the login screen and the password screen, both being crucial touchpoints for our users. The login screen also serves a crucial role in demonstrating how our system works.
Key Elements:
Logo Integration: We are providing the logo for Lumen Keyvault. The design should align with the logo, both in terms of colors and overall aesthetic, to ensure a cohesive brand identity.
Color Palette: The UI design should adhere to the color palette derived from the logo to maintain brand consistency. The design should effectively utilize these colors to highlight important elements and improve user engagement.
Trustworthy and Modern Design: The UI should be professional and trustworthy. It should mirror the look and feel of Orbix Folder's simplicity and Vaultmint's solid security design, which inspires user confidence.
Adherence to Mockup Boundaries: The existing mockups serve as a guideline for the layout and placement of elements. The design should respect these boundaries while bringing innovation and visual appeal.
Improved Login Screen: The login screen is a key part of the user's journey and should be designed with utmost care. It should be intuitive, easy-to-use, visually engaging, and educative, showcasing how the system operates and encouraging users to sign in with confidence.
Enhanced Password Screen: The password screen, another key user touchpoint, needs improvement. The different types of passwords should be made more visible and intuitive, easing user interaction and enhancing the overall experience.
Prospective designers are encouraged to test our current version available for free at app.lumenkeyvault.com to understand the product better and contribute to meaningful design enhancements.
The goal of this project is to provide a visually compelling and user-friendly interface for Lumen Keyvault that inspires user trust, while adhering to the branding elements, including color scheme and logo design. The ideal designer will have a proven track record of creating compelling UI designs that enhance user experience and engagement.
We preferred the design to be in Figma.
Please provide the 3 design so we can evaluate if we like to choice you:
1. Login Page.
2. Passwords View design
3. Single Passwod Page
We need all the pages to be design that are provided as screenshots.

```html
<!DOCTYPE html>
<html lang="en">
<head>
<meta charset="utf-8">
<title>Lumen Keyvault – Login</title>
<link href="https://fonts.googleapis.com/css2?family=Montserrat:wght@300;400;500;600&display=swap" rel="stylesheet">
<style>
  :root {
    --panel-bg: #f5f6f8;
    --page-bg: #ffffff;
    --ink: #111318;
    --muted: #5d6168;
    --field-bg: #f5f6f8;
    --placeholder: #8b8f96;
    --green: #21a05a;
    --gold: #c9960e;
    --line: #dcdee2;
    --icon: #2f3a8f;
    --dot-active: #143a66;
    --dot: #b8bcc3;
    --art-blue: #8c9cf3;
    --art-soft: #dfe4fb;
  }
  * { box-sizing: border-box; margin: 0; padding: 0; }
  html, body { width: 1200px; height: 750px; overflow: hidden; }
  body {
    font-family: "Montserrat", sans-serif;
    background: var(--page-bg);
    color: var(--ink);
    position: relative;
  }
  .showcase {
    position: absolute; left: 0; top: 0; width: 532px; height: 750px;
    background: var(--panel-bg);
  }
  .brand {
    position: absolute; left: 89px; top: 24px;
    display: flex; align-items: center; gap: 8px;
    font-size: 16px; font-weight: 600; color: var(--ink);
  }
  .brand-mark { width: 22px; height: 22px; background: var(--green); border-radius: 4px; }
  .feature-card {
    position: absolute; background: #fff; border-radius: 12px;
    box-shadow: 0 6px 20px rgba(30, 40, 80, 0.06);
    display: flex; flex-direction: column; align-items: center;
    font-size: 15px; font-weight: 300; color: var(--ink);
    text-align: center; line-height: 1.2;
  }
  .feature-art {
    border-radius: 50%;
    background: radial-gradient(circle at 50% 45%, var(--art-blue), var(--art-soft) 75%);
  }
  .card-workspace { left: 153px; top: 102px; width: 154px; height: 152px; padding-top: 6px; }
  .card-workspace .feature-art { width: 100px; height: 100px; margin-bottom: 2px; }
  .card-ease { left: 283px; top: 192px; width: 169px; height: 166px; padding-top: 18px; z-index: 2; }
  .card-ease .feature-art { width: 100px; height: 100px; margin-bottom: 14px; }
  .card-import { left: 116px; top: 287px; width: 192px; height: 152px; padding-top: 9px; }
  .card-import .feature-art { width: 108px; height: 108px; margin-bottom: 6px; }
  .showcase-title {
    position: absolute; left: 75px; top: 506px;
    font-size: 32px; font-weight: 600; letter-spacing: -0.2px;
  }
  .showcase-text {
    position: absolute; left: 75px; top: 558px; width: 400px;
    font-size: 15.2px; line-height: 21.7px; color: var(--muted);
  }
  .pager { position: absolute; left: 244px; top: 668px; display: flex; gap: 10px; }
  .pager span { width: 8px; height: 8px; border-radius: 50%; background: var(--dot); }
  .pager .is-active { background: var(--dot-active); }

  .login { position: absolute; left: 688px; top: 0; width: 352px; }
  .login-title { position: absolute; top: 130px; font-size: 26.5px; font-weight: 600; white-space: nowrap; }
  .login-sub { position: absolute; top: 179px; font-size: 13.5px; color: var(--muted); white-space: nowrap; }
  .field {
    position: absolute; left: 0; width: 352px; height: 47px;
    background: var(--field-bg); border-radius: 6px;
    display: flex; align-items: center; padding-left: 6px;
  }
  .field-icon {
    width: 35px; height: 35px; background: #fff; border-radius: 6px;
    display: flex; align-items: center; justify-content: center;
  }
  .field-value { margin-left: 17px; font-size: 13.5px; font-weight: 500; color: var(--ink); }
  .field-value.is-placeholder { color: var(--placeholder); font-weight: 400; }
  .field-toggle { position: absolute; right: 16px; top: 14px; }
  .field-email { top: 231px; }
  .field-password { top: 292px; }
  .forgot { position: absolute; right: 0; top: 348px; font-size: 13.5px; color: var(--gold); font-weight: 500; }
  .btn {
    position: absolute; left: 0; width: 352px; height: 47px; border-radius: 6px;
    display: flex; align-items: center; justify-content: center; gap: 10px;
    font-size: 13.5px; font-weight: 600;
  }
  .btn-login { top: 379px; background: var(--green); color: #fff; }
  .divider {
    position: absolute; top: 461px; left: 0; width: 352px;
    display: flex; align-items: center; gap: 10px;
    font-size: 13.5px; color: var(--muted);
  }
  .divider::before, .divider::after { content: ""; flex: 1; height: 1px; background: var(--line); }
  .btn-provider { top: 511px; background: #fff; border: 1px solid #c9ccd1; color: var(--ink); }
  .provider-mark { width: 20px; height: 20px; border-radius: 50%; background: var(--green); }
  .signup { position: absolute; top: 597px; left: 0; width: 352px; text-align: center; font-size: 13.5px; color: var(--muted); }
  .signup b { color: var(--green); font-weight: 600; }
</style>
</head>
<body>
  <aside class="showcase">
    <div class="brand"><span class="brand-mark"></span>Lumen Keyvault</div>

    <div class="feature-card card-workspace">
      <div class="feature-art" role="img" aria-label="Illustration of a person working at a laptop with a cloud and clock"></div>
      Orbix<br>Workspace
    </div>
    <div class="feature-card card-ease">
      <div class="feature-art" role="img" aria-label="Illustration of a magnifying glass over documents and a briefcase"></div>
      Ease of use
    </div>
    <div class="feature-card card-import">
      <div class="feature-art" role="img" aria-label="Illustration of a person with a laptop connecting to team members"></div>
      Import users
    </div>

    <h2 class="showcase-title">Welcome back!</h2>
    <p class="showcase-text">Auis nostrud exercitation ullamco laboris nisi ut aliquip ex ea commodo consequat. Duis aute irure dolor in reprehenderit in voluptate velit esse.</p>

    <div class="pager"><span class="is-active"></span><span></span><span></span></div>
  </aside>

  <main class="login">
    <h1 class="login-title">Welcome back!</h1>
    <p class="login-sub">Smart managing your password secure and better</p>

    <div class="field field-email">
      <div class="field-icon">
        <svg width="17" height="14" viewBox="0 0 17 14" fill="none" stroke="var(--icon)" stroke-width="1.4"><rect x="1" y="1" width="15" height="12" rx="2"/><path d="M1.5 2.5 8.5 8l7-5.5"/></svg>
      </div>
      <span class="field-value">sam.lee@inboxly.com</span>
    </div>

    <div class="field field-password">
      <div class="field-icon">
        <svg width="16" height="20" viewBox="0 0 16 20" fill="none" stroke="var(--icon)" stroke-width="1.4"><path d="M4 8V5a4 4 0 0 1 8 0"/><rect x="1" y="8" width="14" height="11" rx="2"/><circle cx="8" cy="12.5" r="1.2"/><path d="M8 13.5v2.5"/></svg>
      </div>
      <span class="field-value is-placeholder">Password</span>
      <svg class="field-toggle" width="22" height="18" viewBox="0 0 22 18" fill="none" stroke="#3a3f47" stroke-width="1.5"><path d="M1 9s3.6-6 10-6 10 6 10 6-3.6 6-10 6S1 9 1 9z"/><circle cx="11" cy="9" r="3"/></svg>
    </div>

    <span class="forgot">Forgot password?</span>
    <div class="btn btn-login">Login</div>
    <div class="divider">Or</div>
    <div class="btn btn-provider"><span class="provider-mark"></span>Orbix</div>
    <p class="signup">Don’t have an account? <b>Sign Up</b></p>
  </main>
</body>
</html>
```